Maple Cove Laser Dermal Studio needs an 8 page WP redesign

We need a colorful re-design for an 8 page Wordpress website. The current preliminary website is live. The home page URL is http://maplecovelaserdermalstudio.com The new logo is live on the website also. I would like a (re)design using the colors that are represented by the new logo file, and any additional complimentary colors. The information regarding the business can be found on the website already, so please review it for insight. The name of the business is "Maple Cove Laser Dermal Studio".

Target Market(s)

The targeted website viewer is an adult female between the ages of 30 and 75 who is interested in facial renewal, wart removal and scar removal. This website should inspire in the target viewer the benefits of laser facial renewal, wart removal and new scar removal. Potential website viewers are wanting and searching for improved skin health and appearance. The website must represent the essence of a professional spa business.

Industry/Entity Type

Business

Font styles to use
Sans Serif

Requirements
Must have
• - The phone number placed in a visible and high value widget area that allows mobile phone browser dialing.

```html
<!DOCTYPE html>
<html lang="en">
<head>
<meta charset="utf-8">
<title>Maple Cove Laser Dermal Studio</title>
<link href="https://fonts.googleapis.com/css2?family=Arimo:wght@400&family=Krona+One&family=Quicksand:wght@400;500&family=Open+Sans:wght@400;700&family=Roboto+Condensed:wght@400;700&display=swap" rel="stylesheet">
<style>
:root{
  --night:#220f23;
  --plum:#5c2a5c;
  --magenta:#a12fb2;
  --heading:#a52eb8;
  --ink:#222;
  --panel:#dedede;
  --white:#fff;
  --muted:#9a9a9a;
}
*{margin:0;padding:0;box-sizing:border-box}
html,body{width:981px;height:1200px;overflow:hidden}
body{background:var(--plum);font-family:"Arimo",Arial,sans-serif;color:var(--ink);position:relative}
.top-band{position:absolute;left:0;top:0;width:981px;height:164px;background:var(--night)}
.brand{position:absolute;left:86px;top:34px;display:flex;align-items:center;gap:10px;color:var(--white);font-family:"Open Sans",sans-serif;font-weight:700;font-size:19px;line-height:22px;text-decoration:none}
.brand-dot{width:34px;height:34px;border-radius:50%;background:var(--magenta);flex:none}
.info{position:absolute;top:40px;display:flex;gap:8px;color:var(--white);font-family:"Open Sans",sans-serif;font-size:10.5px;line-height:15px;text-decoration:none}
.info b{font-weight:700}
.info.shipping{left:576px}
.info.call{left:758px}
.sheet{position:absolute;left:82px;top:118px;width:818px;height:1002px;background:var(--white)}
.nav{position:absolute;left:85px;top:121px;width:811px;height:39px;background:var(--magenta);border-bottom:4px solid #c35ad2;display:flex;justify-content:space-between;padding:0 16px;list-style:none}
.nav li{font-size:12.5px;color:var(--white);line-height:35px;position:relative}
.nav li.active::after{content:"";position:absolute;left:-16px;right:-16px;bottom:-4px;height:4px;background:var(--night)}
.hero{position:absolute;left:86px;top:164px;width:810px;height:372px;background:linear-gradient(100deg,#8da2b1 0%,#8a9fae 45%,#c9b3a5 62%,#8ea3b2 80%,#7e95a6 100%)}
.hero-title{position:absolute;left:109px;top:228px;font-family:"Krona One",sans-serif;font-size:26px;color:var(--night);font-weight:400;white-space:nowrap}
.hero-tag{position:absolute;left:102px;top:283px;width:288px;height:53px;padding:0 13px;background:rgba(200,210,218,.85);font-family:"Quicksand",sans-serif;font-size:31px;color:var(--heading);line-height:53px;white-space:nowrap}
.hero-guarantee{position:absolute;left:103px;top:346px;font-family:"Open Sans",sans-serif;font-size:29px;color:var(--white)}
.hero-text{position:absolute;left:109px;top:390px;width:300px;font-size:10.8px;line-height:16.5px;color:var(--white)}
.order{position:absolute;left:107px;top:440px;width:103px;height:48px;border:3px solid #c9d3dc;border-radius:5px;background:#dfe3e6;font-size:13px;color:var(--ink);line-height:42px;text-align:center}
h2.section{position:absolute;font-family:"Quicksand",sans-serif;font-weight:500;color:var(--heading);font-size:20.5px;white-space:nowrap}
p.body{position:absolute;font-size:10.3px;line-height:16.4px}
.portrait{position:absolute;left:96px;top:678px;width:199px;height:200px;border:1px solid #c57bd0;background:linear-gradient(135deg,#fff 0%,#f2dccd 45%,#c99a82 70%,#fff 100%)}
.providers{position:absolute;left:95px;top:910px;font-family:"Quicksand",sans-serif;font-weight:500;color:var(--heading);font-size:14px;white-space:nowrap}
.services{position:absolute;left:97px;top:946px;width:500px;list-style:none;font-size:9.8px;line-height:12px}
.services li{position:absolute;left:0;padding-left:10px;width:490px}
.services li::before{content:"•";position:absolute;left:0;top:0}
.sidebar{position:absolute;left:665px;top:540px;width:230px;height:545px;background:var(--panel)}
.special{position:absolute;left:673px;top:546px;width:217px;height:37px;background:var(--plum);color:var(--white);font-family:"Roboto Condensed",sans-serif;font-weight:400;font-size:16px;letter-spacing:-0.3px;line-height:37px;padding-left:4px;white-space:nowrap}
.event{position:absolute;left:674px;width:215px;height:57px;background:var(--white);font-family:"Open Sans",sans-serif;padding:12px 0 0 4px}
.event .date{font-size:10px;font-weight:700;color:var(--ink);line-height:13px}
.event .title{font-size:9.4px;color:var(--muted);line-height:15px}
.event svg{position:absolute;right:6px;top:18px}
.recent{position:absolute;left:679px;top:749px;font-family:"Quicksand",sans-serif;font-size:15.5px;color:#444;font-weight:500}
.post-photo{position:absolute;left:679px;top:777px;width:162px;height:80px;background:linear-gradient(135deg,#6b4a3a,#a8735a 50%,#c8b3a2)}
.post-caption{position:absolute;left:677px;top:862px;font-family:"Roboto Condensed",sans-serif;font-weight:700;font-size:12px;color:#555}
.post-list{position:absolute;left:678px;top:889px;list-style:none;font-family:"Open Sans",sans-serif;font-size:10px;color:#333}
.post-list li{height:25.3px;display:flex;align-items:center;gap:10px}
.post-list li::before{content:"";width:10px;height:10px;border-radius:50%;background:#555}
.footer{position:absolute;left:82px;top:1120px;width:818px;height:80px;background:var(--night);color:var(--white)}
.footer-links{position:absolute;left:14px;top:18px;font-size:11px;display:flex;gap:9px}
.copyright{position:absolute;left:13px;top:44px;font-size:11px}
.footer-brand{position:absolute;left:620px;top:22px;display:flex;align-items:center;gap:8px;font-family:"Open Sans",sans-serif;font-weight:700;font-size:14px;line-height:17px}
.footer-brand .brand-dot{width:26px;height:26px}
</style>
</head>
<body>
<div class="top-band"></div>
<a class="brand" href="http://maplecovelaserdermalstudio.com"><span class="brand-dot"></span><span>Maple Cove Laser<br>Dermal Studio</span></a>

<div class="info shipping">
  <svg width="27" height="27" viewBox="0 0 27 27"><circle cx="13.5" cy="13.5" r="11.5" fill="none" stroke="#fff" stroke-width="2.5"/><path d="M13.5 7v7h5" fill="none" stroke="#fff" stroke-width="2.5"/></svg>
  <div><b>24HR SHIPPING</b><br>Free for UK Customers</div>
</div>
<a class="info call" href="tel:1800456627537">
  <svg width="22" height="28" viewBox="0 0 22 28"><path d="M5 2l4 0 1 6-3 2c1 4 3 8 6 11l3-2 5 4-2 4c-7 0-16-10-16-20z" fill="#fff"/></svg>
  <div><b>CALL TOLL FREE</b><br>1800 - 456 - MAPLEDS</div>
</a>

<div class="sheet"></div>
<ul class="nav">
  <li class="active">Home</li><li>About Us</li><li>Skin Renewal</li><li>Scar Removal</li><li>Wart Removal</li><li>Your Visit</li><li>Contact Us</li><li>Blog</li>
</ul>

<div class="hero" role="img" aria-label="Portrait of a woman touching her face with white feathers floating on a soft blue-grey backdrop"></div>
<h1 class="hero-title">Maple Cove Laser</h1>
<div class="hero-tag">Dermal Studio</div>
<div class="hero-guarantee">100 % GUARANTEE</div>
<p class="hero-text">Lorem Ipsum is simply dummy text of the printing and type-setting industry.</p>
<div class="order">ORDER NOW</div>

<h2 class="section" style="left:96px;top:554px">Have you considered Laser Skin Renewal Therapy?</h2>
<p class="body" style="left:96px;top:590px;width:537px">You will truly love laser skin renewal if your skin is showing signs of premature aging or the skin has sustained sun damage. Conditions such as excessive redness due to sun exposure or fine lines will be concerns of the past. In fact, laser skin therapy is a unique and innovative way to enjoy youthful and healthy skin without resort-ing to painful and inconvenient surgery. Both men and women are receiving benefits from laser skin therapy.</p>

<div class="portrait" role="img" aria-label="Portrait of a smiling woman with bare shoulders"></div>
<h2 class="section" style="left:313px;top:672px">Laser Skin Renewal is Innovative</h2>
<p class="body" style="left:313px;top:701px;width:318px">The literature contains ample scientific evidence to support laser skin renewal. After this therapy, your skin will produce collagen, which reduces and minimizes the appearance of fine lines and wrinkles. Imagine getting all this with minimal pain and no downtime? Doesn't it make you feel like getting in touch with our laser skin specialist today?<br><br>Conditions such as excessive redness due to sun exposure or fine lines will be concerns of the past. In fact, laser skin therapy is a unique and innovative way to enjoy youthful and healthy skin without resorting to painful and inconvenient surgery.</p>

<h3 class="providers">The Bright Path Vision Centers and Dr. Helena Marsh provide:</h3>
<ul class="services">
  <li style="top:0">Comprehensive Eye Examinations for All Ages, including Infants and Preschoolers</li>
  <li style="top:25px">Vision Therapy for All Ages</li>
  <li style="top:49px">Treatment for Learning-related Vision Problems</li>
  <li style="top:81px">Free Monthly Seminars. Visit our Cove Circle page for information about our free monthly seminars on a variety of topics, including: The Hidden Disability - Undiagnosed Vision Problems</li>
</ul>

<aside class="sidebar"></aside>
<div class="special">New Years Resolution Special!</div>
<div class="event" style="top:594px"><div class="date">22 DECEMBER 2013</div><div class="title">MUST-GROW NEW PERENNIALS FOR 2013</div><svg width="12" height="20" viewBox="0 0 12 20"><path d="M2 2l8 8-8 8" fill="none" stroke="#aaa" stroke-width="3"/></svg></div>
<div class="event" style="top:664px"><div class="date">22 DECEMBER 2013</div><div class="title">MUST-GROW NEW PERENNIALS FOR 2013</div><svg width="12" height="20" viewBox="0 0 12 20"><path d="M2 2l8 8-8 8" fill="none" stroke="#aaa" stroke-width="3"/></svg></div>
<h3 class="recent">Recent Posts</h3>
<div class="post-photo" role="img" aria-label="Sepia portrait of a woman with long hair"></div>
<div class="post-caption">Muyatse byaserta verotas:</div>
<ul class="post-list">
  <li>ASETY KSCABO</li><li>NERAFAES</li><li>KERTYU ERSVITA ERTYA</li><li>SNEMO LASEC VASP</li><li>TAIADES GOERTAYSE</li><li>VOLERNATUR AUT</li><li>ODITAU JAIUSE</li>
</ul>

<footer class="footer">
  <div class="footer-links"><span>Home</span><span>|</span><span>About Us</span><span>|</span><span>Skin Renewal</span><span>|</span><span>Scar Removal</span><span>|</span><span>Wart Removal</span><span>|</span><span>Your Visit</span><span>|</span><span>Contact Us</span><span>|</span><span>Blog</span></div>
  <div class="copyright">Copyright © 2014 All Rights Reserved | Privacy Policy</div>
  <div class="footer-brand"><span class="brand-dot"></span><span>Maple Cove Laser<br>Dermal Studio</span></div>
</footer>
</body>
</html>
```